Lobby Sentinel Staffing

Lobby sentinel is similar to a security company but is more concierge/customer service oriented. Picture a security guard in a suit working at a condo or office building. Our thoughts for a logo is a silhouette of a male/female sitting at a desk or some type of crest but were open to creative ideas.

Target Market(s)

Property Managers

Industry/Entity Type

Security

Font styles to use
Serif

Requirements
Must have
• Male/Female sitting professionally at a desk.
Nice to have
• Vertical card
Should not have
• Cartoons

```html
<!DOCTYPE html>
<html lang="en">
<head>
<meta charset="utf-8">
<title>Lobby Sentinel Staffing – Business Card</title>
<link href="https://fonts.googleapis.com/css2?family=Exo+2:wght@400;500;600;700&display=swap" rel="stylesheet">
<style>
  :root{
    --backdrop:#2b2a2a;
    --card:#ffffff;
    --brand-red:#e3161e;
    --ink:#2a2a2a;
    --band:#d4d4d4;
    --icon-bg:#3a3a3a;
    --icon-fg:#ffffff;
    --ring:#4a4a4a;
  }
  html,body{margin:0;padding:0;width:1200px;height:1200px;overflow:hidden;background:var(--backdrop);}
  .card{
    position:absolute;left:330px;top:150px;width:540px;height:900px;
    background:var(--card);border-radius:22px;overflow:hidden;
    font-family:"Exo 2",sans-serif;color:var(--ink);
  }
  .emblem{
    position:absolute;left:155px;top:90px;width:230px;height:230px;border-radius:50%;
    border:3px solid var(--ring);box-sizing:border-box;
    background:linear-gradient(180deg,#ffffff 0%,#ffffff 45%,#6a6a6a 46%,#3c3c3c 100%);
  }
  .company{
    position:absolute;left:0;right:0;top:360px;text-align:center;
    color:var(--brand-red);font-weight:600;font-size:36px;letter-spacing:0.5px;text-transform:uppercase;
    white-space:nowrap;
  }
  .person{position:absolute;left:0;right:0;top:455px;text-align:center;}
  .person-name{color:var(--brand-red);font-weight:600;font-size:30px;text-transform:uppercase;line-height:1.1;}
  .person-role{font-weight:700;font-size:24px;line-height:1.2;}
  .contacts{position:absolute;left:0;right:0;top:570px;margin:0;padding:0;list-style:none;}
  .contact-row{height:50px;display:flex;align-items:center;font-size:23px;white-space:nowrap;}
  .contact-row:nth-child(odd){background:var(--band);}
  .contact-icon{width:36px;height:36px;margin:0 26px 0 40px;background:var(--icon-bg);display:flex;align-items:center;justify-content:center;flex:none;}
  .contact-icon svg{width:24px;height:24px;fill:none;stroke:var(--icon-fg);stroke-width:1.8;stroke-linecap:round;stroke-linejoin:round;}
</style>
</head>
<body>
  <div class="card">
    <div class="emblem" role="img" aria-label="Silhouette of a professional in a suit seated at a reception desk with a computer monitor"></div>
    <div class="company">Lobby Sentinel Staffing</div>
    <div class="person">
      <div class="person-name">Daniel Hart</div>
      <div class="person-role">General Manager</div>
    </div>
    <ul class="contacts">
      <li class="contact-row">
        <span class="contact-icon"><svg viewBox="0 0 24 24"><path d="M6 3l3 4-2 2c1 3 4 6 7 7l2-2 4 3-2 3C11 20 4 13 3 5z"/></svg></span>
        +1 541 208 3176
      </li>
      <li class="contact-row">
        <span class="contact-icon"><svg viewBox="0 0 24 24"><rect x="7" y="2" width="10" height="20" rx="2"/><path d="M11 18h2"/></svg></span>
        +1 541 774 0925
      </li>
      <li class="contact-row">
        <span class="contact-icon"><svg viewBox="0 0 24 24"><rect x="7" y="3" width="10" height="6"/><rect x="3" y="9" width="18" height="8"/><rect x="7" y="14" width="10" height="7"/></svg></span>
        +1 541 208 3190
      </li>
      <li class="contact-row">
        <span class="contact-icon"><svg viewBox="0 0 24 24"><rect x="3" y="6" width="18" height="12"/><path d="M3 6l9 7 9-7"/></svg></span>
        danielhart@mail.com
      </li>
      <li class="contact-row">
        <span class="contact-icon"><svg viewBox="0 0 24 24"><circle cx="12" cy="12" r="9"/><path d="M3 12h18M12 3c3 3 3 15 0 18M12 3c-3 3-3 15 0 18"/></svg></span>
        www.lobbysentinelstaffing.com
      </li>
      <li class="contact-row">
        <span class="contact-icon"><svg viewBox="0 0 24 24"><path d="M12 21s-6-6-6-11a6 6 0 0112 0c0 5-6 11-6 11z"/><circle cx="12" cy="10" r="2"/></svg></span>
        210 Harbor Ave., Elmont, OR 97402
      </li>
    </ul>
  </div>
</body>
</html>
```